Marco Vessi Landing page

I need a Landing page for a website Marco Vessi. This is for an upscale clothing store for Men and Womens clothing and other items. It has to be elegant and unique in design and style.

Target Market(s)

Men, Women, Young adults 18-60

Coding

Number of Pages Required

1 page

Font styles to use
Decorative

Colors

Designer to choose colors to be used in the design.

```html
<!DOCTYPE html>
<html lang="en">
<head>
<meta charset="utf-8">
<title>Marco Vessi — Landing Page</title>
<link rel="stylesheet" href="https://fonts.googleapis.com/css2?family=Cinzel:wght@400;600&family=Playfair+Display:wght@700&family=Montserrat:wght@400;500;600&display=swap">
<style>
  :root{
    --ink:#1b1b1b;
    --ink-2:#121212;
    --ink-3:#2a2a2a;
    --gold:#c9a45c;
    --gold-soft:#e2c98f;
    --page:#f2f2f2;
    --card:#ffffff;
    --text:#444444;
    --muted:#8a8a8a;
    --line:#d8d8d8;
    --white:#ffffff;
  }
  *{box-sizing:border-box;margin:0;padding:0}
  html,body{width:1200px;height:2268px;overflow:hidden}
  body{position:relative;background:var(--page);font-family:"Montserrat",sans-serif;color:var(--text)}

  /* Sidebar */
  .sidebar{position:absolute;left:0;top:0;width:288px;height:2068px;background:var(--ink)}
  .brand{text-align:center;padding-top:30px}
  .brand-mark{display:block;width:44px;height:44px;margin:0 auto 12px;border:2px solid var(--gold)}
  .brand-name{font-family:"Cinzel",serif;font-size:30px;font-weight:400;color:var(--gold);letter-spacing:1px}
  .brand-tag{font-size:10px;letter-spacing:2px;color:var(--gold-soft);margin-top:4px;text-transform:uppercase}
  .menu{list-style:none;margin-top:66px}
  .menu li{height:28px;line-height:28px;padding-left:120px;font-size:11px;font-weight:500;letter-spacing:1px;color:var(--white);text-transform:uppercase}
  .menu li.active{background:var(--gold-soft);color:var(--ink);margin:0 30px;padding-left:90px}
  .tools{display:flex;justify-content:center;gap:22px;margin-top:30px}
  .select{margin:24px auto 0;width:220px;height:30px;background:var(--white);font-size:10px;color:var(--muted);line-height:30px;padding-left:10px;position:relative}
  .select::after{content:"";position:absolute;right:10px;top:12px;border:5px solid transparent;border-top-color:var(--ink)}
  .follow{text-align:center;margin-top:54px;font-size:12px;font-weight:600;letter-spacing:1px;color:var(--white);text-transform:uppercase}
  .social{display:flex;justify-content:center;gap:12px;margin-top:14px}
  .social span{width:14px;height:14px;border-radius:50%;background:var(--gold)}

  /* Hero */
  .hero{position:absolute;left:288px;top:0;width:912px;height:660px;background:linear-gradient(90deg,#9a8bbf 0%,#b7aedb 45%,#d9d2ef 100%)}
  .hero-photo{position:absolute;right:60px;top:0;width:380px;height:660px;background:linear-gradient(180deg,#6f7fa8 0%,#3d5a86 55%,#2e3f63 100%)}
  .hero-copy{position:absolute;left:62px;top:196px;color:var(--white)}
  .hero-kicker{font-size:17px;margin-bottom:10px}
  .hero-title{font-family:"Playfair Display",serif;font-size:62px;line-height:1.04;font-weight:700;text-transform:uppercase}
  .btn-dark{display:inline-block;margin-top:22px;background:var(--ink-3);color:var(--white);font-size:14px;padding:10px 22px;text-transform:uppercase;letter-spacing:1px}

  /* Products */
  .tabs{position:absolute;left:348px;top:672px;display:flex;gap:46px;font-size:11px;font-weight:500;letter-spacing:1px;color:var(--ink);text-transform:uppercase}
  .tabs-rule{position:absolute;left:288px;top:696px;width:912px;height:1px;background:var(--line)}
  .card{position:absolute;width:252px;height:252px;background:var(--card)}
  .card .shot{position:absolute;left:66px;top:66px;width:120px;height:120px;border-radius:10px}
  .btn-outline{position:absolute;left:698px;top:1570px;width:104px;height:30px;border:1px solid var(--ink);font-size:10px;line-height:28px;text-align:center;color:var(--ink);text-transform:uppercase;letter-spacing:1px}

  /* News */
  .news-title{position:absolute;left:288px;top:1690px;width:912px;text-align:center;font-family:"Playfair Display",serif;font-size:26px;color:var(--ink)}
  .news-lede{position:absolute;left:540px;top:1734px;width:420px;text-align:center;font-size:10px;line-height:16px;color:var(--muted)}
  .news-img{position:absolute;top:1800px;height:180px}

  /* Footer */
  .footer{position:absolute;left:0;top:2068px;width:1200px;height:172px;background:var(--ink-2);color:#bdbdbd;font-size:10px;line-height:16px}
  .f-brand{position:absolute;left:330px;top:22px;font-family:"Cinzel",serif;color:var(--gold);font-size:18px}
  .f-about{position:absolute;left:330px;top:70px;width:200px}
  .f-head{position:absolute;top:50px;color:var(--gold);font-size:12px;font-weight:600}
  .f-contact{position:absolute;left:582px;top:76px;width:220px}
  .f-social{position:absolute;left:842px;top:80px;display:flex;gap:8px}
  .f-social span{width:18px;height:18px;border-radius:50%;border:1px solid var(--gold)}
  .to-top{position:absolute;left:1064px;top:26px;width:34px;height:34px;border-radius:50%;border:1px solid var(--gold)}
  .bottom-bar{position:absolute;left:0;top:2240px;width:1200px;height:28px;background:var(--ink-3);font-size:9px;color:#9a9a9a;line-height:28px}
  .bottom-bar .copy{position:absolute;left:330px}
  .bottom-bar .links{position:absolute;left:870px;display:flex;gap:22px}
</style>
</head>
<body>

<aside class="sidebar">
  <div class="brand">
    <span class="brand-mark"></span>
    <div class="brand-name">Marco Vessi</div>
    <div class="brand-tag">Fashion House</div>
  </div>
  <ul class="menu">
    <li class="active">Home</li>
    <li>About</li>
    <li>Shop</li>
    <li>Collections</li>
    <li>Blog</li>
    <li>Contact</li>
  </ul>
  <div class="tools">
    <svg width="14" height="14" viewBox="0 0 14 14"><circle cx="6" cy="6" r="4.5" fill="none" stroke="#c9a45c" stroke-width="1.6"/><line x1="9.5" y1="9.5" x2="13" y2="13" stroke="#c9a45c" stroke-width="1.6"/></svg>
    <svg width="14" height="14" viewBox="0 0 14 14"><rect x="2" y="4" width="10" height="9" fill="none" stroke="#c9a45c" stroke-width="1.4"/><path d="M4.5 4V3a2.5 2.5 0 0 1 5 0v1" fill="none" stroke="#c9a45c" stroke-width="1.4"/></svg>
    <svg width="14" height="14" viewBox="0 0 14 14"><circle cx="7" cy="7" r="6" fill="#c0392b"/></svg>
    <svg width="14" height="14" viewBox="0 0 14 14"><circle cx="7" cy="4.5" r="3" fill="none" stroke="#c9a45c" stroke-width="1.4"/><path d="M1.5 13c1-3 3-4 5.5-4s4.5 1 5.5 4" fill="none" stroke="#c9a45c" stroke-width="1.4"/></svg>
  </div>
  <div class="select">Select Menu</div>
  <div class="follow">Follow Us</div>
  <div class="social"><span></span><span></span><span></span><span></span><span></span></div>
</aside>

<section class="hero">
  <div class="hero-photo" role="img" aria-label="Bearded man in sunglasses and a denim shirt"></div>
  <div class="hero-copy">
    <div class="hero-kicker">Welcome to Marco Vessi</div>
    <h1 class="hero-title">New Men<br>Collection<br>2019</h1>
    <span class="btn-dark">Shop Now</span>
  </div>
</section>

<nav class="tabs"><span>Accessories</span><span>Shoes</span><span>Bag</span><span>Decoration</span></nav>
<div class="tabs-rule"></div>

<div class="card" style="left:348px;top:728px"><div class="shot" role="img" aria-label="Wooden bowls" style="background:linear-gradient(#c08a55,#8a5a30)"></div></div>
<div class="card" style="left:620px;top:728px"><div class="shot" role="img" aria-label="Grey sneaker" style="background:linear-gradient(#9a9a9a,#6d6d6d)"></div></div>
<div class="card" style="left:892px;top:728px"><div class="shot" role="img" aria-label="White chair with wooden legs" style="background:linear-gradient(#f1f1f1,#d9c7a8)"></div></div>
<div class="card" style="left:348px;top:1000px"><div class="shot" role="img" aria-label="Tobacco pipe" style="background:linear-gradient(#c8632a,#2a2a2a)"></div></div>
<div class="card" style="left:620px;top:1000px"><div class="shot" role="img" aria-label="Blue pencil holder with pencils" style="background:linear-gradient(#e6b54a,#58a6dd)"></div></div>
<div class="card" style="left:892px;top:1000px"><div class="shot" role="img" aria-label="Black sunglasses" style="background:linear-gradient(#3a3a3a,#111)"></div></div>
<div class="card" style="left:348px;top:1280px"><div class="shot" role="img" aria-label="Black wall clock" style="background:radial-gradient(circle,#f5f5f5 45%,#1f1f1f 60%);border-radius:50%"></div></div>
<div class="card" style="left:620px;top:1280px"><div class="shot" role="img" aria-label="White headphones" style="background:linear-gradient(#eeeeee,#b9a58c)"></div></div>
<div class="card" style="left:892px;top:1280px"><div class="shot" role="img" aria-label="Leather football" style="background:linear-gradient(#b06a35,#6e3a18);border-radius:50%"></div></div>

<span class="btn-outline">View More</span>

<h2 class="news-title">Latest News</h2>
<p class="news-lede">Fresh stories from our studio on style, craft and the season ahead, written for the modern wardrobe.</p>
<div class="news-img" role="img" aria-label="Pastel yellow and lilac desk flat lay" style="left:428px;width:192px;background:linear-gradient(135deg,#f3dc8a,#d9c9e6)"></div>
<div class="news-img" role="img" aria-label="White desk with notebook" style="left:640px;width:188px;background:linear-gradient(135deg,#f4f4f4,#dcdcdc)"></div>
<div class="news-img" role="img" aria-label="Desk corner with cup and pen" style="left:848px;width:192px;background:linear-gradient(135deg,#ededed,#cfcfcf)"></div>

<footer class="footer">
  <div class="f-brand">Marco Vessi</div>
  <p class="f-about">Join the discount club and stay informed about new arrivals and updates.</p>
  <div class="f-head" style="left:582px">Contact Us</div>
  <p class="f-contact">Your Address or street info goes here<br>Mail: hello@marcovessi.com<br>Phone: 000 0000 000</p>
  <div class="f-head" style="left:842px">Follow Us</div>
  <div class="f-social"><span></span><span></span><span></span><span></span><span></span></div>
  <svg class="to-top" viewBox="0 0 34 34"><path d="M11 19l6-6 6 6" fill="none" stroke="#c9a45c" stroke-width="1.6"/></svg>
</footer>
<div class="bottom-bar">
  <span class="copy">© 2019 Marco Vessi. All Rights Reserved.</span>
  <span class="links"><span>Our Services</span><span>Privacy</span><span>Website</span></span>
</div>

</body>
</html>
```